BRL business card

For a business card with our logo

Contact Information for Business Card

Mathéo VRANEL
Founder & CEO
email : ceo@brightlanterncollective.com / www.brightlanterncollective.com /
instagram / facebook / WhatsApp
N°: +590 690 482 517

Colors

Designer to choose colors to be used in the design.

```html
<!DOCTYPE html>
<html lang="en">
<head>
<meta charset="utf-8">
<title>BRL business card</title>
<link rel="stylesheet" href="https://fonts.googleapis.com/css2?family=Merriweather:wght@400;700;900&display=swap">
<style>
  :root {
    --backdrop: #2b2d31;
    --card: #222325;
    --card-edge: #1f5fc4;
    --brand-blue: #1f63c8;
    --brand-orange: #f07a22;
    --text-light: #e9e9e9;
  }
  * { margin: 0; padding: 0; box-sizing: border-box; }
  html, body { width: 1200px; height: 900px; overflow: hidden; }
  body {
    background: var(--backdrop);
    font-family: "Merriweather", Georgia, serif;
    display: flex; flex-direction: column; align-items: center; justify-content: center;
    gap: 56px;
  }
  .card {
    position: relative;
    width: 620px; height: 354px;
    background: var(--card);
    border-bottom: 5px solid var(--card-edge);
    box-shadow: 0 14px 30px rgba(0,0,0,.45);
  }
  .brand { position: absolute; display: flex; align-items: center; gap: 14px; }
  .brand-dot { border-radius: 50%; background: var(--brand-orange); flex: none; }
  .brand-name {
    color: var(--brand-blue); font-weight: 700; text-transform: uppercase;
    letter-spacing: .06em; line-height: 1.25;
  }
  /* back */
  .card-back .brand { left: 50%; top: 50%; transform: translate(-50%, -50%); }
  .card-back .brand-dot { width: 84px; height: 84px; }
  .card-back .brand-name { font-size: 24px; }
  /* front */
  .card-front .brand { left: 40px; top: 40px; }
  .card-front .brand-dot { width: 52px; height: 52px; }
  .card-front .brand-name { font-size: 15px; }
  .person { position: absolute; left: 300px; top: 150px; }
  .person-name { font-size: 26px; font-weight: 900; letter-spacing: .04em; }
  .person-name .first { color: var(--brand-orange); }
  .person-name .last { color: var(--brand-blue); }
  .person-role { color: var(--text-light); font-size: 12px; letter-spacing: .25em; margin-top: 4px; }
  .divider { position: absolute; left: 270px; top: 206px; width: 2px; height: 70px; background: var(--brand-orange); }
  .contacts { position: absolute; left: 290px; top: 212px; list-style: none; }
  .contacts li {
    display: flex; align-items: center; gap: 10px;
    color: var(--text-light); font-size: 12px; font-weight: 700; margin-bottom: 9px;
  }
  .contacts svg { width: 16px; height: 16px; flex: none; stroke: var(--brand-orange); fill: none; stroke-width: 1.6; }
  .socials { position: absolute; left: 290px; top: 316px; display: flex; gap: 22px; }
  .socials span { display: flex; align-items: center; gap: 6px; color: var(--brand-orange); font-size: 11px; }
  .socials i { width: 12px; height: 12px; border: 1.6px solid var(--brand-orange); border-radius: 50%; }
</style>
</head>
<body>
  <section class="card card-back">
    <div class="brand">
      <span class="brand-dot"></span>
      <span class="brand-name">Bright Lantern<br>Collective</span>
    </div>
  </section>

  <section class="card card-front">
    <div class="brand">
      <span class="brand-dot"></span>
      <span class="brand-name">Bright Lantern<br>Collective</span>
    </div>

    <div class="person">
      <div class="person-name"><span class="first">MATHÉO</span> <span class="last">VRANEL</span></div>
      <div class="person-role">Founder &amp; CEO</div>
    </div>

    <span class="divider"></span>
    <ul class="contacts">
      <li><svg viewBox="0 0 16 16"><rect x="4" y="1.5" width="8" height="13" rx="1.5"/><line x1="7" y1="12" x2="9" y2="12"/></svg>+590 690 482 517</li>
      <li><svg viewBox="0 0 16 16"><rect x="1.5" y="3.5" width="13" height="9"/><polyline points="1.5,3.5 8,9 14.5,3.5"/></svg>ceo@brightlanterncollective.com</li>
      <li><svg viewBox="0 0 16 16"><circle cx="8" cy="8" r="6.5"/><ellipse cx="8" cy="8" rx="3" ry="6.5"/><line x1="1.5" y1="8" x2="14.5" y2="8"/></svg>www.brightlanterncollective.com</li>
      <li><svg viewBox="0 0 16 16"><path d="M8 1.5a6.5 6.5 0 1 1-3.4 12L1.5 14.5l1-3A6.5 6.5 0 0 1 8 1.5z"/></svg>+590 690 482 517</li>
    </ul>
    <div class="socials">
      <span><i></i>photo profile</span>
      <span><i></i>social page</span>
    </div>
  </section>
</body>
</html>
```